Photographer website

This website will contain information to sell the services of marvento quillas an up and coming photographer based in london
Updates

Target Market(s)

SME's for corporate head shots
mums for kids parties
actors - for headshots
up and coming models

Industry/Entity Type

Photographer

Number of Pages Required

3 page

Requirements
Must have
• Home
• About me
• Contact me
• Portfolio or gallery

```html
<!DOCTYPE html>
<html lang="en">
<head>
<meta charset="utf-8">
<title>Quilla — Portrait Photography</title>
<link href="https://fonts.googleapis.com/css2?family=Delius&family=Raleway:wght@400;500&family=Signika:wght@600&display=swap" rel="stylesheet">
<style>
:root{
  --teal:#0e8a80;
  --teal-dark:#0b746c;
  --ink:#2b2b2b;
  --muted:#6b6b6b;
  --line:#e3e3e3;
  --dark:#1f1f1f;
  --white:#ffffff;
}
*{margin:0;padding:0;box-sizing:border-box}
html,body{width:819px;height:1200px;overflow:hidden;background:var(--white)}
body{position:relative;font-family:'Raleway',sans-serif;color:var(--ink)}
.header{position:absolute;left:0;top:0;width:819px;height:90px}
.topbar{position:absolute;right:0;top:0;width:241px;height:30px;background:var(--dark);
  clip-path:polygon(0 0,100% 0,100% 100%,16px 100%);display:flex;align-items:center;justify-content:flex-end;gap:20px;padding-right:30px;
  font-family:'Delius',cursive;font-size:8px;color:#ddd}
.topbar span{display:flex;align-items:center;gap:5px}
.brand{position:absolute;left:30px;top:22px;font-family:'Delius',cursive;font-size:34px;color:var(--ink);display:flex;align-items:center;gap:8px}
.brand i{display:block;width:10px;height:10px;background:var(--teal)}
.nav{position:absolute;top:48px;right:30px;display:flex;gap:57px;font-family:'Delius',cursive;font-size:11px}
.nav a{color:var(--ink);text-decoration:none;padding-bottom:10px}
.nav a.active{color:var(--teal);border-bottom:2px solid var(--teal);padding:0 9px 10px}
.hero{position:absolute;left:0;top:90px;width:819px;height:330px;
  background:linear-gradient(90deg,#4a4a4a 0%,#777 35%,#cfcfcf 62%,#8a8a8a 80%,#5c5c5c 100%)}
.hero-copy{position:absolute;left:30px;top:104px;color:var(--white)}
.hero-copy h1{font-family:'Delius',cursive;font-weight:400;font-size:28px;margin-bottom:12px}
.hero-copy p{font-size:11.5px;line-height:17px;width:320px;margin-bottom:14px}
.btn{display:inline-flex;align-items:center;gap:6px;background:var(--teal);color:var(--white);
  font-family:'Signika',sans-serif;font-weight:600;font-size:11px;height:29px;padding:0 16px;border-radius:2px}
.dots{position:absolute;left:378px;top:303px;display:flex;gap:10px}
.dots b{width:8px;height:8px;border-radius:50%;border:1px solid #eee;background:rgba(255,255,255,.3)}
.dots b.on{background:var(--teal);border-color:#eee}
.section-title{position:absolute;left:0;width:819px;text-align:center;font-family:'Delius',cursive;font-size:27px;font-weight:400;color:#3a3a3a}
.section-title em{font-style:normal;color:var(--teal)}
.about-text{position:absolute;left:54px;top:478px;width:716px;text-align:center;font-size:9.6px;line-height:18.7px;color:var(--muted)}
.arrows{position:absolute;left:737px;top:584px;display:flex;gap:7px}
.arrows span{width:23px;height:23px;border-radius:50%;background:var(--teal);display:flex;align-items:center;justify-content:center}
.card{position:absolute;width:238px;height:218px;border:1px solid var(--line);padding:4px;background:var(--white)}
.card.active{border-color:#9fd0cb}
.card .photo{width:100%;height:100%}
.cta{position:absolute;left:358px;top:1113px;height:29px;padding:0 13px}
.cta-shadow{position:absolute;left:360px;top:1147px;width:100px;height:3px;border-radius:50%;background:#ddd}
.footer{position:absolute;left:0;top:1163px;width:819px;height:37px;background:var(--dark);color:#eee;
  display:flex;align-items:center;justify-content:space-between;padding:0 30px;font-size:8.5px}
.footer nav{display:flex;gap:6px}
.social{display:flex;gap:8px}
.social span{width:23px;height:23px;border-radius:50%;border:1px solid #777}
</style>
</head>
<body>
<header class="header">
  <div class="topbar">
    <span><svg width="8" height="6" viewBox="0 0 8 6"><rect width="8" height="6" fill="#0e8a80"/><path d="M0 0L4 3.5L8 0" stroke="#1f1f1f" fill="none"/></svg>studio@quillaphoto.com</span>
    <span><svg width="7" height="7" viewBox="0 0 10 10"><path d="M2 0L4 3L3 4Q4.5 6 6 7L7 6L10 8L8.5 10Q3 9 0 1.5Z" fill="#0e8a80"/></svg>0200 - 7946 - 0312</span>
  </div>
  <div class="brand">Quilla<i></i></div>
  <nav class="nav">
    <a class="active">Home</a><a>About</a><a>Portfolio gallery</a><a>Contact us</a>
  </nav>
</header>

<section class="hero" role="img" aria-label="Black and white portrait of a young woman with long hair">
  <div class="hero-copy">
    <h1>Welcome to Quilla</h1>
    <p>I'm based in London but travel around the globe expecting find that especial picture. Here is a bit of my work.</p>
    <span class="btn">Contact now <svg width="5" height="7" viewBox="0 0 5 7"><path d="M0 0L5 3.5L0 7Z" fill="#fff"/></svg></span>
  </div>
  <div class="dots"><b class="on"></b><b></b><b></b><b></b></div>
</section>

<h2 class="section-title" style="top:436px">About <em>Quilla</em></h2>
<p class="about-text">Hi i am portraiture photographer, I take pictures of people. MQuillas Born in East Brazil, grew up in Spain,. My first years were spent behind why i like this peculiar type of images. I now live in London and I travel to around often.My goal is to show the that little part sometimes we cant appreciate to the quickly eye, well travel shy in the crowds very curious and enthusiasm of people at small groups. I focus on non-models and place regular people in exaggerated situations that highlight an aspect of who they are. I'm based in London but travel around the globe expecting find that especial picture. Here is a bit of my work.</p>

<h2 class="section-title" style="top:576px">Our <em>Portfolio</em></h2>
<div class="arrows">
  <span><svg width="6" height="8" viewBox="0 0 6 8"><path d="M5 0L1 4L5 8" stroke="#fff" stroke-width="1.5" fill="none"/></svg></span>
  <span><svg width="6" height="8" viewBox="0 0 6 8"><path d="M1 0L5 4L1 8" stroke="#fff" stroke-width="1.5" fill="none"/></svg></span>
</div>

<div class="card active" style="left:30px;top:630px"><div class="photo" role="img" aria-label="Colourful cupcakes on a cake stand at a party" style="background:linear-gradient(160deg,#e9e3dc,#cfd9dc 50%,#f1e7cf)"></div></div>
<div class="card" style="left:291px;top:630px"><div class="photo" role="img" aria-label="Portrait of a woman with a braided hairstyle" style="background:linear-gradient(90deg,#e7dcc0,#b9a58c 55%,#2f6a74)"></div></div>
<div class="card" style="left:552px;top:630px"><div class="photo" role="img" aria-label="Model posing in a white blouse and red skirt" style="background:linear-gradient(180deg,#ececec,#dcd6d2 70%,#d33a3a)"></div></div>
<div class="card" style="left:30px;top:870px"><div class="photo" role="img" aria-label="Portrait of a woman with dark curly hair" style="background:linear-gradient(120deg,#3a2b26,#d8b6a4 55%,#ededed)"></div></div>
<div class="card" style="left:291px;top:870px"><div class="photo" role="img" aria-label="Two young girls reading a tablet at a festive party" style="background:linear-gradient(160deg,#8a2a28,#e8d6c6 55%,#efe6dc)"></div></div>
<div class="card" style="left:552px;top:870px"><div class="photo" role="img" aria-label="Black and white portrait of a young woman" style="background:linear-gradient(90deg,#bdbdbd,#9a9a9a 50%,#d8d8d8)"></div></div>

<span class="btn cta">Visit our gallery</span>
<div class="cta-shadow"></div>

<footer class="footer">
  <nav><span>quillaphotography © 2016 .All Rights reserved</span><span>/</span><span>About</span><span>/</span><span>Gallery</span><span>/</span><span>contact us</span></nav>
  <div class="social">
    <span aria-label="Social profile"></span><span aria-label="Social profile"></span><span aria-label="Social profile"></span><span aria-label="Social profile"></span>
  </div>
</footer>
</body>
</html>
```